Business Coaching Model and Flow Chart

We need this flowchart, attached, to be updated in a modern and engaging way. This flowchart is the cornerstone of a business coaching class we are running, and will be the main support reference for the people who take the class. We are open to ideas as to how it is presented, but we would like a largely minimalist look that leaves space to be impactful where the key information sites. Our colour scheme is primary red (D51C29), white, grey (333333), black, and secondary green (3C8740). We will also need our logo present (attached).

```html
<!DOCTYPE html>
<html lang="en">
<head>
<meta charset="utf-8">
<title>Groups to Teams Through Learning Together</title>
<link href="https://fonts.googleapis.com/css2?family=Roboto+Condensed:wght@300;400;500;700&display=swap" rel="stylesheet">
<style>
:root{
  --red:#d51c29;
  --ink:#333333;
  --green:#3c8740;
  --tint:#d0e3d2;
  --paper:#ffffff;
  --backdrop:#2e2e2e;
}
*{margin:0;padding:0;box-sizing:border-box}
html,body{width:1200px;height:942px;overflow:hidden;background:var(--backdrop)}
body{font-family:"Roboto Condensed",sans-serif;color:var(--ink)}
.poster{position:absolute;left:280px;top:18px;width:1013px;height:1433px;background:var(--paper);transform:scale(.632);transform-origin:0 0;box-shadow:0 8px 30px rgba(0,0,0,.45)}
.at{position:absolute;line-height:1.1;white-space:nowrap}
.mid{transform:translate(-50%,-50%);text-align:center}
.left{transform:translateY(-50%)}
.band{position:absolute;left:0;width:1013px;height:162px}
.band--tint{background:var(--tint)}
.band--last{height:218px}

.brand{left:70px;top:67px}
.brand__disc{position:absolute;left:-36px;top:-36px;width:72px;height:72px;border-radius:50%;background:var(--red)}
.brand__name{position:absolute;left:0;top:42px;transform:translateX(-50%);color:var(--red);font-weight:700;font-size:12px;letter-spacing:.5px;text-transform:uppercase;white-space:nowrap}
.title{left:505px;top:118px;font-size:54px;font-weight:700;line-height:1.1;text-transform:uppercase}
.rule{position:absolute;left:116px;top:181px;width:776px;height:5px;background:var(--red)}
.rule__dot{position:absolute;left:497px;top:173px;width:20px;height:20px;border-radius:50%;background:var(--ink)}

.step{position:absolute;width:48px;height:48px;margin:-24px 0 0 -24px;border-radius:50%;background:var(--red);color:#fff;font-size:36px;font-weight:300;display:flex;align-items:center;justify-content:center}
.heading{font-size:52px;font-weight:700;text-transform:uppercase}
.stage{font-size:29px;font-weight:500;text-transform:uppercase;line-height:1.12}
.point{font-size:23px;font-weight:500;text-transform:uppercase;line-height:1.12}
.point--dot::before,.note--dot::before{content:"";display:inline-block;border-radius:50%;background:var(--green);vertical-align:middle}
.point--dot::before{width:11px;height:11px;margin:0 6px 4px 0}
.note{font-size:13.5px;text-transform:uppercase}
.note--dot::before{width:5px;height:5px;margin:0 5px 2px 0}
.tag{font-size:13px;text-transform:uppercase;text-align:center;line-height:1.1;transform:translateX(-50%)}
.icon{position:absolute;width:42px;height:42px;transform:translateX(-50%)}
.icon--red{fill:var(--red);stroke:var(--red)}
.icon--green{fill:var(--green);stroke:var(--green)}
</style>
</head>
<body>
<main class="poster">

  <header>
    <div class="at brand"><span class="brand__disc"></span><span class="brand__name">Mara Lowell</span></div>
    <h1 class="at mid title">Groups to Teams<br>Through Learning Together</h1>
    <span class="rule"></span><span class="rule__dot"></span>
  </header>

  <section class="band band--tint" style="top:243px">
    <span class="step" style="left:63px;top:82px">1</span>
    <h2 class="at left heading" style="left:110px;top:82px">Problem</h2>

    <svg class="icon icon--red" style="left:401px;top:16px" viewBox="0 0 40 40"><rect x="8" y="4" width="24" height="32" fill="none" stroke-width="2.5"/><path d="M13 12h14M13 18h14M13 24h8" stroke-width="2"/></svg>
    <span class="at tag" style="left:401px;top:64px">Underbilling</span>
    <svg class="icon icon--red" style="left:573px;top:14px" viewBox="0 0 40 40"><circle cx="16" cy="16" r="11" fill="none" stroke-width="4"/><path d="M24 24l11 11" stroke-width="6"/></svg>
    <span class="at tag" style="left:573px;top:64px">Hard to recruit</span>
    <svg class="icon icon--red" style="left:736px;top:12px" viewBox="0 0 40 40"><circle cx="20" cy="20" r="18" stroke="none"/></svg>
    <span class="at tag" style="left:736px;top:64px">Staff stress &amp; burnout</span>
    <svg class="icon icon--red" style="left:881px;top:14px" viewBox="0 0 40 40"><path d="M4 26l14-6-2 4 18-4-16 10 2-4z" stroke="none"/><path d="M36 10L22 16l2-4-14 2 14-8-2 4z" stroke="none"/></svg>
    <span class="at tag" style="left:881px;top:64px">Sector constant<br>change</span>

    <svg class="icon icon--red" style="left:481px;top:86px" viewBox="0 0 40 40"><circle cx="20" cy="12" r="7" stroke="none"/><circle cx="8" cy="16" r="5" stroke="none"/><circle cx="32" cy="16" r="5" stroke="none"/><path d="M8 36c0-10 24-10 24 0z M0 34c0-8 10-9 12-6 M40 34c0-8-10-9-12-6" stroke="none"/></svg>
    <span class="at tag" style="left:481px;top:136px">Staff retention</span>
    <svg class="icon icon--red" style="left:651px;top:84px" viewBox="0 0 40 40"><path d="M4 4h32v24H20l-8 8v-8H4z" stroke="none"/><path d="M20 9v11M20 23v3" stroke="#fff" stroke-width="3"/></svg>
    <span class="at tag" style="left:651px;top:136px">Client complaints</span>
    <svg class="icon icon--red" style="left:810px;top:86px" viewBox="0 0 40 40"><path d="M22 4l-8 16h8l-4 16 10-20h-8z" stroke="none"/><path d="M2 20h8M30 20h8M6 8l6 6M34 8l-6 6M6 32l6-6M34 32l-6-6" stroke-width="2" fill="none"/></svg>
    <span class="at tag" style="left:810px;top:136px">Conflict</span>
    <svg class="icon icon--red" style="left:960px;top:80px" viewBox="0 0 40 40"><path d="M9 3h22v4l-8 13 8 13v4H9v-4l8-13-8-13z" fill="none" stroke-width="3"/><path d="M13 33l7-9 7 9z" stroke="none"/></svg>
    <span class="at tag" style="left:960px;top:126px">Limited in<br>best practice</span>
  </section>

  <section class="band" style="top:405px">
    <p class="at left point point--dot" style="left:47px;top:54px">Scoping</p>
    <p class="at left point point--dot" style="left:47px;top:124px">Interviews</p>
    <p class="at left point point--dot" style="left:207px;top:54px">Group reflection</p>
    <p class="at left point point--dot" style="left:207px;top:124px">Opinion surveys</p>
    <p class="at left point point--dot" style="left:440px;top:58px">Certified<br>&nbsp;&nbsp;&nbsp;Assessments</p>
    <p class="at left note note--dot" style="left:428px;top:95px">Personality styles</p>
    <p class="at left note note--dot" style="left:428px;top:114px">Work preference</p>
    <p class="at left note note--dot" style="left:428px;top:133px">Strengths &amp; values</p>
    <p class="at left note note--dot" style="left:572px;top:101px">Trust</p>
    <p class="at left note note--dot" style="left:572px;top:118px">360</p>
    <span class="step" style="left:679px;top:90px">2</span>
    <h2 class="at mid stage" style="left:854px;top:90px">Clarify challenges -<br>diagnostics</h2>
  </section>

  <section class="band band--tint" style="top:567px">
    <span class="step" style="left:63px;top:82px">3</span>
    <h2 class="at mid stage" style="left:254px;top:84px">Planning for success<br>make a plan</h2>
    <p class="at mid point point--dot" style="left:589px;top:44px">Team data<br>analysis workshops</p>
    <p class="at mid point point--dot" style="left:589px;top:107px">Individual<br>development plan</p>
    <p class="at mid point point--dot" style="left:863px;top:44px">Team<br>development plan</p>
    <p class="at mid point point--dot" style="left:863px;top:107px">Organizational<br>plan</p>
  </section>

  <section class="band" style="top:729px">
    <p class="at left point point--dot" style="left:100px;top:43px">Foundation<br>&nbsp;&nbsp;&nbsp;Workshops</p>
    <p class="at left note note--dot" style="left:104px;top:82px">Difficult conversation</p>
    <p class="at left note note--dot" style="left:104px;top:110px">Giving &amp; recieving feedback</p>
    <p class="at left note note--dot" style="left:104px;top:137px">Values alignment</p>
    <p class="at left note note--dot" style="left:312px;top:28px">Shared purpose</p>
    <p class="at left note note--dot" style="left:312px;top:56px">Ways of working</p>
    <p class="at left note note--dot" style="left:312px;top:82px">Diversity</p>
    <p class="at left note note--dot" style="left:312px;top:108px">Wellbeing</p>
    <p class="at left note note--dot" style="left:312px;top:135px">Time management</p>
    <p class="at mid point point--dot" style="left:568px;top:88px">Customized<br>workshops</p>
    <span class="step" style="left:732px;top:81px">4</span>
    <h2 class="at mid stage" style="left:882px;top:82px">Learn the tools<br>workshops</h2>
  </section>

  <section class="band band--tint" style="top:891px">
    <span class="step" style="left:63px;top:82px">5</span>
    <h2 class="at mid stage" style="left:218px;top:83px">Doing mastering<br>the tools</h2>
    <p class="at left point point--dot" style="left:362px;top:60px">Group coaching</p>
    <p class="at left point point--dot" style="left:370px;top:100px">Team coaching</p>
    <p class="at left point point--dot" style="left:576px;top:60px">Individual coaching</p>
    <p class="at left point point--dot" style="left:606px;top:100px">Peer learning</p>
    <p class="at left point point--dot" style="left:820px;top:83px">Lunch ‘n learn</p>
  </section>

  <section class="band" style="top:1053px">
    <p class="at left note note--dot" style="left:32px;top:36px;font-size:16px">Culture committee</p>
    <p class="at left note note--dot" style="left:32px;top:66px;font-size:16px">Embedding workshop</p>
    <p class="at left note note--dot" style="left:32px;top:97px;font-size:16px">Culture collateral</p>
    <p class="at left note note--dot" style="left:32px;top:128px;font-size:16px">Wow manifesto</p>
    <p class="at left note note--dot" style="left:224px;top:36px;font-size:16px">Leadership team coaching</p>
    <p class="at left note note--dot" style="left:224px;top:66px;font-size:16px">Measure ROI</p>
    <p class="at left note note--dot" style="left:224px;top:97px;font-size:16px">Review success</p>
    <p class="at left note note--dot" style="left:224px;top:128px;font-size:16px">Evaluation surveys</p>
    <p class="at left note note--dot" style="left:455px;top:36px;font-size:16px">Temperature checks</p>
    <p class="at left note note--dot" style="left:455px;top:66px;font-size:16px">Recruit to suit</p>
    <p class="at left note note--dot" style="left:455px;top:97px;font-size:16px">Future proofing -</p>
    <p class="at left note" style="left:468px;top:128px;font-size:16px">What next?</p>
    <span class="step" style="left:666px;top:75px">6</span>
    <h2 class="at left stage" style="left:702px;top:75px">Reflect - adapt - embed</h2>
  </section>

  <section class="band band--tint band--last" style="top:1215px">
    <span class="step" style="left:63px;top:80px">7</span>
    <h2 class="at left heading" style="left:106px;top:80px">Solution</h2>

    <svg class="icon icon--green" style="left:394px;top:22px" viewBox="0 0 40 40"><circle cx="20" cy="11" r="9" stroke="none"/><path d="M3 38c0-16 34-16 34 0z" stroke="none"/></svg>
    <span class="at tag" style="left:394px;top:66px">Self awareness<br>&amp; ownership</span>
    <svg class="icon icon--green" style="left:548px;top:22px;width:56px" viewBox="0 0 56 40"><rect x="4" y="18" width="48" height="14" stroke="none"/><circle cx="14" cy="8" r="5" stroke="none"/><circle cx="28" cy="8" r="5" stroke="none"/><circle cx="42" cy="8" r="5" stroke="none"/><path d="M8 32v6M48 32v6" stroke-width="3"/></svg>
    <span class="at tag" style="left:548px;top:66px">Great place to work</span>
    <svg class="icon icon--green" style="left:693px;top:20px" viewBox="0 0 40 40"><path d="M4 16h8l16-10v28L12 24H4z" stroke="none"/><path d="M12 24l4 12h5l-3-12" stroke="none"/><path d="M32 14c3 3 3 9 0 12" fill="none" stroke-width="3"/></svg>
    <span class="at tag" style="left:693px;top:66px">Coach approach<br>culture</span>
    <svg class="icon icon--green" style="left:862px;top:18px" viewBox="0 0 40 40"><circle cx="20" cy="20" r="11" fill="none" stroke-width="7" stroke-dasharray="5 3"/><circle cx="20" cy="20" r="4" stroke="none"/></svg>
    <span class="at tag" style="left:862px;top:66px">Way to manage<br>conflict</span>

    <svg class="icon icon--green" style="left:471px;top:84px" viewBox="0 0 40 40"><path d="M2 18l10-8 8 4 8-4 10 8-6 6-12 8-12-8z" stroke="none"/></svg>
    <span class="at tag" style="left:471px;top:131px">Partnership</span>
    <svg class="icon icon--green" style="left:628px;top:82px" viewBox="0 0 40 40"><path d="M20 36V20" stroke-width="3" fill="none"/><path d="M20 20c-2-10-12-12-16-10 2 8 10 12 16 10zM20 16c2-9 10-12 16-10-2 8-10 12-16 10z" stroke="none"/><path d="M4 36h32" stroke-width="4"/></svg>
    <span class="at tag" style="left:628px;top:131px">Growth mindset</span>
    <svg class="icon icon--green" style="left:787px;top:80px;width:56px" viewBox="0 0 56 40"><path d="M2 4h52v26H18l-8 8v-8H2z" stroke="none"/><path d="M14 17h6M25 17h6M36 17h6" stroke="#fff" stroke-width="5" stroke-linecap="round"/></svg>
    <span class="at tag" style="left:787px;top:131px">Feedback culture</span>
    <svg class="icon icon--green" style="left:950px;top:40px" viewBox="0 0 40 40"><path d="M4 6h22v16H14l-6 6v-6H4z" fill="none" stroke-width="2"/><path d="M16 26h10l2-4h8v14h-4v4l-6-4H16z" fill="none" stroke-width="2"/></svg>
    <span class="at tag" style="left:950px;top:92px">Best practice<br>communication<br>skills</span>
  </section>

</main>
</body>
</html>
```